MORVANT EU Project PowerPoint Template

Please Provide a PowerPoint template to be used for a European project. The main scope of the project is to support research organisations across Europe to design and implement gender equality plans in order to promote the women’s position of the filed of STEM research.
The Power Point template is going to be used by the entire consortium of the project (approx. 50 people) and it is going to be used to deliver official reports to the Continental Directorate and in real -life events like international Conferences etc. Therefore, the design has to be professional and official. Given that the PowerPoint template is going to be utilised by several people simultaneously, the document should afford each user to add elements (tables, etc.) that have the same format. Any time the user adds bullet points, these should have a particular colour and shape, and so on. Please note the Consortium members are both MS Windows and MAC users.
In terms of layout, please consult the colour combination of the attached logo, to design a template with matching colour patterns. Attached to this project description you may find a generic PowerPoint template for the project just as an example. Pay notice to the bottom of each slide, where a specific phrase along with the EU flag must be included. Please, keep the phrase as it is; you my find images for the EU flag here: https://velmoria.example/union/about/symbols/flag_en.
In addition, two more presentation templates from previous projects are provided as examples. You may have a good look at them too.
For any questions and/or clarifications feel free to contact.

```html
<!DOCTYPE html>
<html lang="en">
<head>
<meta charset="utf-8">
<title>MORVANT – Presentation Deck</title>
<link href="https://fonts.googleapis.com/css2?family=Montserrat:wght@300;400;500;600;700;800&display=swap" rel="stylesheet">
<style>
:root{
  --purple:#5a4a9e;
  --purple-dark:#3f3380;
  --lilac:#a9a1d6;
  --lilac-soft:#e6e2f5;
  --gold:#f2b705;
  --gold-soft:#f8d86a;
  --ink:#3a3a48;
  --grey:#9a9aa8;
  --line:#dcdce4;
  --page:#ffffff;
  --flag:#1f3f99;
}
*{box-sizing:border-box;margin:0;padding:0}
html,body{width:1200px;height:2684px;overflow:hidden;background:var(--page)}
body{position:relative;font-family:"Montserrat",sans-serif;color:var(--ink)}

/* ---------- header ---------- */
.hero-photo{position:absolute;left:0;top:0;width:1200px;height:520px;
  background:linear-gradient(180deg,#8f8cb0 0%,#b9b6cf 35%,#e6e4ef 70%,#ffffff 100%)}
.hero-band{position:absolute;left:0;top:330px;width:600px;height:150px;
  background:linear-gradient(90deg,rgba(255,255,255,.85),rgba(255,255,255,.2))}
.brand{position:absolute;left:70px;top:48px;display:flex;align-items:center;gap:16px}
.brand-dot{width:62px;height:62px;border-radius:50%;background:var(--gold)}
.brand-name{font-weight:500;font-size:52px;letter-spacing:4px;color:var(--purple)}
.brand-tag{position:absolute;left:148px;top:118px;font-size:16px;color:#fff;font-weight:500}
.deck-title{position:absolute;left:70px;top:345px;line-height:1}
.deck-title .main{display:block;font-size:58px;font-weight:700;color:var(--purple)}
.deck-title .sub{display:block;font-size:52px;font-weight:400;color:var(--ink);margin-top:10px}
.hero-slide{position:absolute;left:600px;top:70px;width:560px;height:315px;
  box-shadow:0 10px 30px rgba(40,30,90,.25)}
.section-label{position:absolute;left:0;top:640px;width:1200px;text-align:center;
  font-size:26px;font-weight:400;color:var(--purple)}
.section-label::before{content:"";position:absolute;left:50%;top:-22px;width:600px;margin-left:-300px;
  border-top:1px solid var(--line)}

/* ---------- slide thumbnails ---------- */
.slide{position:absolute;width:336px;height:189px;background:#fff;overflow:hidden;
  box-shadow:0 2px 8px rgba(40,30,90,.18)}
.c1{left:44px}.c2{left:432px}.c3{left:820px}
.slide .mini-brand{position:absolute;right:10px;top:8px;font-size:7px;font-weight:600;
  letter-spacing:1px;color:var(--purple);display:flex;align-items:center;gap:3px}
.mini-brand::before{content:"";width:7px;height:7px;border-radius:50%;background:var(--gold)}
.slide .foot{position:absolute;left:0;bottom:0;width:100%;height:14px;display:flex;align-items:center;
  gap:5px;padding-left:10px;font-size:4.5px;color:var(--grey);border-top:1px solid #efeff4}
.foot .flag{width:12px;height:8px;background:var(--flag)}
.s-title{position:absolute;font-weight:700;color:var(--purple);font-size:13px;line-height:1.1}
.s-sub{position:absolute;font-size:6px;color:var(--grey)}
.t{position:absolute;font-size:5px;line-height:1.5;color:var(--grey)}
.t b{color:var(--ink);font-weight:600;font-size:6px;display:block}
.center{left:0;width:100%;text-align:center}
.logo-lock{position:absolute;display:flex;align-items:center;gap:8px}
.logo-lock .dot{border-radius:50%;background:var(--gold)}
.logo-lock .nm{color:var(--purple);font-weight:500;letter-spacing:2px}
.ph{position:absolute}
.bar{position:absolute;height:8px;border-radius:1px}
.tbl{position:absolute;border-collapse:collapse;font-size:4.5px;color:var(--ink)}
.tbl th{background:var(--purple);color:#fff;font-weight:600;padding:3px 4px;text-align:left}
.tbl td{padding:3px 4px;border-bottom:1px solid var(--line)}
.tbl tr:nth-child(even) td{background:var(--lilac-soft)}
.num{position:absolute;width:16px;height:16px;border-radius:50%;color:#fff;font-size:7px;font-weight:700;
  display:flex;align-items:center;justify-content:center}
.list{position:absolute;list-style:none;font-size:5.5px;color:var(--ink);line-height:2.1}
.list li::before{content:"";display:inline-block;width:5px;height:5px;background:var(--gold);margin-right:5px;vertical-align:middle}
.list.purple li::before{background:var(--purple);border-radius:50%}
.chip{position:absolute;background:#eceaf4;border-radius:2px}
</style>
</head>
<body>

<!-- ===== header ===== -->
<div class="hero-photo" role="img" aria-label="Soft photo of a crowd of people against a bright sky"></div>
<div class="hero-band"></div>
<div class="brand"><span class="brand-dot"></span><span class="brand-name">MORVANT</span></div>
<div class="brand-tag">Gender Equality in STEM Research</div>
<h1 class="deck-title"><span class="main">Presentation</span><span class="sub">Deck</span></h1>

<div class="hero-slide slide" style="width:560px;height:315px">
  <span class="mini-brand" style="font-size:11px;top:14px;right:16px">MORVANT</span>
  <div class="s-title" style="right:150px;top:40px;font-size:22px">Two Facts</div>
  <div class="s-sub" style="right:150px;top:68px;font-size:8px">Add a short subtitle here</div>
  <div class="ph" style="left:150px;top:95px;width:170px;height:150px;background:var(--purple);padding:18px;color:#fff;font-size:11px;font-weight:700;line-height:1.35">GENDER EQUALITY IS NOT ONLY A MATTER OF SOCIAL JUSTICE BUT ALSO OF RESEARCH PERFORMANCE</div>
  <div class="ph" role="img" aria-label="Illustration of gender symbols beside a small figure" style="left:300px;top:100px;width:150px;height:140px;background:radial-gradient(circle,#c9c3e8,#f3d98a 60%,#fff 80%)"></div>
  <div class="foot" style="height:22px;font-size:7px"><span class="flag" style="width:20px;height:13px"></span><span>Funded under grant agreement 000000</span></div>
</div>

<div class="section-label">Powerpoint Presentation</div>

<!-- ===== row 1 : title slides ===== -->
<div class="slide c1" style="top:700px">
  <div class="t" style="left:10px;top:8px">Project meeting · Add date here</div>
  <div class="logo-lock" style="left:60px;top:70px"><span class="dot" style="width:26px;height:26px"></span><span class="nm" style="font-size:22px">MORVANT</span></div>
  <div class="t" style="left:96px;top:100px">Gender Equality in STEM Research</div>
  <div class="foot"><span class="flag"></span><span>Funded under grant agreement 000000</span></div>
</div>
<div class="slide c2" style="top:700px">
  <div class="logo-lock" style="left:24px;top:75px"><span class="dot" style="width:22px;height:22px"></span><span class="nm" style="font-size:17px">MORVANT</span></div>
  <div class="t" style="left:190px;top:74px"><b>Presentation title</b>Speaker name<br>Event and place</div>
  <div class="foot"><span class="flag"></span><span>Funded under grant agreement 000000</span></div>
</div>
<div class="slide c3" style="top:700px">
  <div class="t center" style="top:8px">Project meeting · Add date here</div>
  <div class="logo-lock" style="left:82px;top:64px"><span class="dot" style="width:26px;height:26px"></span><span class="nm" style="font-size:22px">MORVANT</span></div>
  <div class="t center" style="top:98px">Gender Equality in STEM Research</div>
  <div class="foot"><span class="flag"></span><span>Funded under grant agreement 000000</span></div>
</div>

<!-- ===== row 2 ===== -->
<div class="slide c1" style="top:898px">
  <span class="mini-brand">MORVANT</span>
  <div class="s-title" style="left:24px;top:78px;font-size:15px">Project Introduction</div>
  <div class="s-sub" style="left:24px;top:98px">Add a short subtitle here</div>
  <div class="foot"><span class="flag"></span><span>Funded under grant agreement 000000</span></div>
</div>
<div class="slide c2" style="top:898px">
  <div class="logo-lock" style="left:110px;top:40px"><span class="dot" style="width:16px;height:16px"></span><span class="nm" style="font-size:13px">MORVANT</span></div>
  <div class="s-title center" style="top:84px;font-size:17px;font-weight:400">Project Introduction</div>
  <div class="s-sub center" style="top:106px">Add a short subtitle here</div>
  <div class="foot"><span class="flag"></span><span>Funded under grant agreement 000000</span></div>
</div>
<div class="slide c3" style="top:898px">
  <svg class="ph" style="left:-50px;top:20px" width="170" height="170"><circle cx="85" cy="85" r="70" fill="none" stroke="var(--lilac-soft)" stroke-width="18"/></svg>
  <div class="s-title" style="left:36px;top:84px;font-size:16px;font-weight:400;color:var(--lilac)">Agenda</div>
  <ol class="list" style="left:200px;top:36px"><li>Introduction</li><li>Objectives</li><li>Work plan</li><li>Partners</li><li>Results</li><li>Next steps</li></ol>
  <div class="foot"><span class="flag"></span><span>Funded under grant agreement 000000</span></div>
</div>

<!-- ===== row 3 ===== -->
<div class="slide c1" style="top:1096px">
  <span class="mini-brand">MORVANT</span>
  <div class="s-title" style="left:24px;top:82px;font-size:16px">Agenda</div>
  <ol class="list purple" style="left:170px;top:36px"><li>Introduction</li><li>Objectives</li><li>Work plan</li><li>Partners</li><li>Results</li><li>Next steps</li></ol>
  <div class="foot"><span class="flag"></span><span>Funded under grant agreement 000000</span></div>
</div>
<div class="slide c2" style="top:1096px">
  <div class="ph" role="img" aria-label="Photo of a group of people at an event" style="left:0;top:0;width:336px;height:78px;background:linear-gradient(180deg,#9c98b8,#d9d6e6)"></div>
  <div class="s-title" style="left:20px;top:92px">Your Text Here</div>
  <div class="t" style="left:20px;top:112px;width:140px">Add a short paragraph that sums up the topic of this slide.</div>
  <div class="t" style="left:180px;top:92px;width:140px">Add a short paragraph that supports the main point here.</div>
  <div class="foot"><span class="flag"></span><span>Funded under grant agreement 000000</span></div>
</div>
<div class="slide c3" style="top:1096px">
  <span class="mini-brand">MORVANT</span>
  <div class="s-title" style="left:190px;top:22px">Two Column Text</div>
  <div class="t" style="left:20px;top:56px;width:140px">Add your text here. Keep each column short and clear so the audience can follow the message with ease.</div>
  <div class="t" style="left:176px;top:56px;width:140px">Add your text here. Use this second column for further details, numbers or a short quote.</div>
  <div class="foot"><span class="flag"></span><span>Funded under grant agreement 000000</span></div>
</div>

<!-- ===== row 4 ===== -->
<div class="slide c1" style="top:1294px">
  <span class="mini-brand">MORVANT</span>
  <div class="s-title" style="left:190px;top:26px">Two Facts</div>
  <div class="ph" style="left:20px;top:50px;width:110px;height:95px;background:var(--purple);padding:10px;color:#fff;font-size:6.5px;font-weight:700;line-height:1.35">GENDER EQUALITY IS NOT ONLY A MATTER OF SOCIAL JUSTICE BUT ALSO OF RESEARCH PERFORMANCE</div>
  <div class="ph" role="img" aria-label="Illustration of gender symbols beside a small figure" style="left:150px;top:54px;width:110px;height:90px;background:radial-gradient(circle,#c9c3e8,#f3d98a 60%,#fff 80%)"></div>
  <div class="foot"><span class="flag"></span><span>Funded under grant agreement 000000</span></div>
</div>
<div class="slide c2" style="top:1294px">
  <span class="mini-brand">MORVANT</span>
  <div class="s-title center" style="top:20px;font-size:11px">Bulleted List Text Sample</div>
  <div class="ph" role="img" aria-label="Female and male gender symbols" style="left:40px;top:50px;width:70px;height:100px;background:linear-gradient(135deg,var(--lilac),var(--gold-soft))"></div>
  <ul class="list" style="left:150px;top:52px"><li>First key point here</li><li>Second key point here</li><li>Third key point here</li><li>Fourth key point here</li></ul>
  <div class="foot"><span class="flag"></span><span>Funded under grant agreement 000000</span></div>
</div>
<div class="slide c3" style="top:1294px">
  <span class="mini-brand">MORVANT</span>
  <div class="s-title center" style="top:18px;font-size:11px">The project</div>
  <svg class="ph" style="left:128px;top:44px" width="80" height="80" viewBox="0 0 80 80">
    <circle cx="40" cy="40" r="28" fill="none" stroke="var(--purple)" stroke-width="14" stroke-dasharray="60 116"/>
    <circle cx="40" cy="40" r="28" fill="none" stroke="var(--gold)" stroke-width="14" stroke-dasharray="55 121" stroke-dashoffset="-62"/>
    <circle cx="40" cy="40" r="28" fill="none" stroke="var(--lilac)" stroke-width="14" stroke-dasharray="55 121" stroke-dashoffset="-119"/>
  </svg>
  <div class="t" style="left:20px;top:54px;width:95px"><b>Design</b>Plans for each partner</div>
  <div class="t" style="left:20px;top:96px;width:95px"><b>Implement</b>Actions in each centre</div>
  <div class="t" style="left:222px;top:54px;width:95px"><b>Monitor</b>Track shared progress</div>
  <div class="t" style="left:222px;top:96px;width:95px"><b>Share</b>Lessons across Europe</div>
  <div class="foot"><span class="flag"></span><span>Funded under grant agreement 000000</span></div>
</div>

<!-- ===== row 5 ===== -->
<div class="slide c1" style="top:1492px">
  <div class="ph" style="left:0;top:0;width:120px;height:175px;background:var(--purple)"></div>
  <div class="s-title" style="left:16px;top:40px;color:#fff">Your Text Here</div>
  <div class="t" style="left:16px;top:60px;width:90px;color:#d9d4f2">Add a short summary line here.</div>
  <div class="chip" style="left:140px;top:34px;width:16px;height:16px;background:var(--gold)"></div>
  <div class="t" style="left:164px;top:34px"><b>Point one</b>Add a short detail</div>
  <div class="chip" style="left:140px;top:74px;width:16px;height:16px;background:var(--lilac)"></div>
  <div class="t" style="left:164px;top:74px"><b>Point two</b>Add a short detail</div>
  <div class="chip" style="left:140px;top:114px;width:16px;height:16px;background:var(--purple)"></div>
  <div class="t" style="left:164px;top:114px"><b>Point three</b>Add a short detail</div>
  <div class="foot" style="padding-left:130px"><span class="flag"></span><span>Funded under grant agreement 000000</span></div>
</div>
<div class="slide c2" style="top:1492px">
  <span class="mini-brand">MORVANT</span>
  <div class="s-title center" style="top:20px;font-size:11px">Training</div>
  <div class="num" style="left:56px;top:52px;background:var(--purple)">1</div>
  <div class="num" style="left:160px;top:52px;background:var(--gold)">2</div>
  <div class="num" style="left:264px;top:52px;background:var(--lilac)">3</div>
  <div class="t" style="left:26px;top:80px;width:80px;text-align:center"><b>Workshop</b>Add a short line here</div>
  <div class="t" style="left:128px;top:80px;width:80px;text-align:center"><b>Webinar</b>Add a short line here</div>
  <div class="t" style="left:232px;top:80px;width:80px;text-align:center"><b>Toolkit</b>Add a short line here</div>
  <div class="foot"><span class="flag"></span><span>Funded under grant agreement 000000</span></div>
</div>
<div class="slide c3" style="top:1492px">
  <span class="mini-brand">MORVANT</span>
  <div class="s-title center" style="top:20px;font-size:11px">Training</div>
  <div class="chip" style="left:30px;top:50px;width:12px;height:12px;background:var(--gold)"></div><div class="t" style="left:48px;top:50px">Topic one here</div>
  <div class="chip" style="left:130px;top:50px;width:12px;height:12px;background:var(--purple)"></div><div class="t" style="left:148px;top:50px">Topic two here</div>
  <div class="chip" style="left:230px;top:50px;width:12px;height:12px;background:var(--gold)"></div><div class="t" style="left:248px;top:50px">Topic three</div>
  <div class="chip" style="left:30px;top:100px;width:12px;height:12px;background:var(--purple)"></div><div class="t" style="left:48px;top:100px">Topic four here</div>
  <div class="chip" style="left:130px;top:100px;width:12px;height:12px;background:var(--gold)"></div><div class="t" style="left:148px;top:100px">Topic five here</div>
  <div class="chip" style="left:230px;top:100px;width:12px;height:12px;background:var(--purple)"></div><div class="t" style="left:248px;top:100px">Topic six</div>
  <div class="foot"><span class="flag"></span><span>Funded under grant agreement 000000</span></div>
</div>

<!-- ===== row 6 ===== -->
<div class="slide c1" style="top:1690px">
  <span class="mini-brand">MORVANT</span>
  <div class="s-title" style="left:20px;top:20px;font-size:11px">Timeline</div>
  <svg class="ph" style="left:20px;top:70px" width="296" height="30">
    <line x1="0" y1="15" x2="296" y2="15" stroke="var(--line)" stroke-width="2"/>
    <circle cx="30" cy="15" r="9" fill="var(--purple)"/><circle cx="110" cy="15" r="9" fill="var(--gold)"/>
    <circle cx="190" cy="15" r="9" fill="var(--purple)"/><circle cx="270" cy="15" r="9" fill="var(--gold)"/>
  </svg>
  <div class="t" style="left:30px;top:48px">2021</div><div class="t" style="left:110px;top:108px">2022</div>
  <div class="t" style="left:190px;top:48px">2023</div><div class="t" style="left:270px;top:108px">2024</div>
  <div class="foot"><span class="flag"></span><span>Funded under grant agreement 000000</span></div>
</div>
<div class="slide c2" style="top:1690px">
  <span class="mini-brand">MORVANT</span>
  <div class="s-title center" style="top:20px;font-size:11px">Timeline</div>
  <svg class="ph" style="left:18px;top:56px" width="300" height="40">
    <polygon points="0,0 66,0 78,20 66,40 0,40 12,20" fill="var(--purple)"/>
    <polygon points="74,0 140,0 152,20 140,40 74,40 86,20" fill="var(--lilac)"/>
    <polygon points="148,0 214,0 226,20 214,40 148,40 160,20" fill="var(--gold)"/>
    <polygon points="222,0 288,0 300,20 288,40 222,40 234,20" fill="var(--gold-soft)"/>
  </svg>
  <div class="t" style="left:30px;top:108px;width:60px">Phase one</div><div class="t" style="left:104px;top:108px;width:60px">Phase two</div>
  <div class="t" style="left:178px;top:108px;width:60px">Phase three</div><div class="t" style="left:252px;top:108px;width:60px">Phase four</div>
  <div class="foot"><span class="flag"></span><span>Funded under grant agreement 000000</span></div>
</div>
<div class="slide c3" style="top:1690px">
  <span class="mini-brand">MORVANT</span>
  <div class="s-title center" style="top:20px;font-size:11px">Our Sponsors</div>
  <div class="chip" style="left:40px;top:50px;width:70px;height:22px"></div><div class="chip" style="left:133px;top:50px;width:70px;height:22px"></div><div class="chip" style="left:226px;top:50px;width:70px;height:22px"></div>
  <div class="chip" style="left:40px;top:84px;width:70px;height:22px"></div><div class="chip" style="left:133px;top:84px;width:70px;height:22px"></div><div class="chip" style="left:226px;top:84px;width:70px;height:22px"></div>
  <div class="chip" style="left:40px;top:118px;width:70px;height:22px"></div><div class="chip" style="left:133px;top:118px;width:70px;height:22px"></div><div class="chip" style="left:226px;top:118px;width:70px;height:22px"></div>
  <div class="foot"><span class="flag"></span><span>Funded under grant agreement 000000</span></div>
</div>

<!-- ===== row 7 ===== -->
<div class="slide c1" style="top:1888px">
  <span class="mini-brand">MORVANT</span>
  <div class="s-title" style="left:20px;top:20px;font-size:11px">Your Text Here</div>
  <svg class="ph" style="left:30px;top:40px" width="120" height="120">
    <polygon points="60,0 80,35 40,35" fill="var(--purple)"/>
    <polygon points="38,39 82,39 100,72 20,72" fill="var(--gold)"/>
    <polygon points="18,76 102,76 120,110 0,110" fill="var(--lilac)"/>
  </svg>
  <div class="t" style="left:170px;top:46px"><b>Level one</b>Add a short line</div>
  <div class="t" style="left:170px;top:84px"><b>Level two</b>Add a short line</div>
  <div class="t" style="left:170px;top:122px"><b>Level three</b>Add a short line</div>
  <div class="foot"><span class="flag"></span><span>Funded under grant agreement 000000</span></div>
</div>
<div class="slide c2" style="top:1888px">
  <span class="mini-brand">MORVANT</span>
  <div class="chip" style="left:40px;top:40px;width:14px;height:14px;background:var(--purple)"></div><div class="t" style="left:62px;top:40px"><b>Item one</b>Add a short line</div>
  <div class="chip" style="left:180px;top:40px;width:14px;height:14px;background:var(--gold)"></div><div class="t" style="left:202px;top:40px"><b>Item two</b>Add a short line</div>
  <div class="chip" style="left:40px;top:90px;width:14px;height:14px;background:var(--gold)"></div><div class="t" style="left:62px;top:90px"><b>Item three</b>Add a short line</div>
  <div class="chip" style="left:180px;top:90px;width:14px;height:14px;background:var(--purple)"></div><div class="t" style="left:202px;top:90px"><b>Item four</b>Add a short line</div>
  <div class="foot"><span class="flag"></span><span>Funded under grant agreement 000000</span></div>
</div>
<div class="slide c3" style="top:1888px">
  <span class="mini-brand">MORVANT</span>
  <div class="s-title center" style="top:18px;font-size:11px">Table</div>
  <table class="tbl" style="left:30px;top:42px;width:276px">
    <tr><th>Partner</th><th>Country</th><th>Role</th><th>Status</th></tr>
    <tr><td>Partner A</td><td>Country</td><td>Lead</td><td>Active</td></tr>
    <tr><td>Partner B</td><td>Country</td><td>Member</td><td>Active</td></tr>
    <tr><td>Partner C</td><td>Country</td><td>Member</td><td>Active</td></tr>
    <tr><td>Partner D</td><td>Country</td><td>Member</td><td>Active</td></tr>
  </table>
  <div class="foot"><span class="flag"></span><span>Funded under grant agreement 000000</span></div>
</div>

<!-- ===== row 8 ===== -->
<div class="slide c1" style="top:2086px">
  <span class="mini-brand">MORVANT</span>
  <div class="s-title" style="left:20px;top:18px;font-size:11px">Table</div>
  <table class="tbl" style="left:20px;top:40px;width:296px">
    <tr><th>Task</th><th>Q1</th><th>Q2</th><th>Q3</th><th>Q4</th></tr>
    <tr><td>Task one</td><td>Yes</td><td>Yes</td><td>No</td><td>No</td></tr>
    <tr><td>Task two</td><td>No</td><td>Yes</td><td>Yes</td><td>No</td></tr>
    <tr><td>Task three</td><td>No</td><td>No</td><td>Yes</td><td>Yes</td></tr>
    <tr><td>Task four</td><td>No</td><td>No</td><td>No</td><td>Yes</td></tr>
  </table>
  <div class="foot"><span class="flag"></span><span>Funded under grant agreement 000000</span></div>
</div>
<div class="slide c2" style="top:2086px">
  <span class="mini-brand">MORVANT</span>
  <div class="s-title center" style="top:18px;font-size:11px">Table</div>
  <div class="t" style="left:30px;top:46px">Item A</div><div class="bar" style="left:70px;top:46px;width:180px;background:var(--purple)"></div>
  <div class="t" style="left:30px;top:64px">Item B</div><div class="bar" style="left:70px;top:64px;width:130px;background:var(--gold)"></div>
  <div class="t" style="left:30px;top:82px">Item C</div><div class="bar" style="left:70px;top:82px;width:220px;background:var(--lilac)"></div>
  <div class="t" style="left:30px;top:100px">Item D</div><div class="bar" style="left:70px;top:100px;width:100px;background:var(--purple)"></div>
  <div class="t" style="left:30px;top:118px">Item E</div><div class="bar" style="left:70px;top:118px;width:160px;background:var(--gold)"></div>
  <div class="foot"><span class="flag"></span><span>Funded under grant agreement 000000</span></div>
</div>
<div class="slide c3" style="top:2086px">
  <span class="mini-brand">MORVANT</span>
  <div class="s-title center" style="top:18px;font-size:11px">Demographic</div>
  <div class="bar" style="left:30px;top:52px;width:50px;height:14px;background:var(--purple)"></div><div class="ph" role="img" aria-label="Row of person pictograms" style="left:90px;top:50px;width:210px;height:18px;background:linear-gradient(90deg,var(--purple) 60%,var(--line) 60%)"></div>
  <div class="bar" style="left:30px;top:86px;width:50px;height:14px;background:var(--gold)"></div><div class="ph" role="img" aria-label="Row of person pictograms" style="left:90px;top:84px;width:210px;height:18px;background:linear-gradient(90deg,var(--gold) 40%,var(--line) 40%)"></div>
  <div class="bar" style="left:30px;top:120px;width:50px;height:14px;background:var(--lilac)"></div><div class="ph" role="img" aria-label="Row of person pictograms" style="left:90px;top:118px;width:210px;height:18px;background:linear-gradient(90deg,var(--lilac) 70%,var(--line) 70%)"></div>
  <div class="foot"><span class="flag"></span><span>Funded under grant agreement 000000</span></div>
</div>

<!-- ===== row 9 ===== -->
<div class="slide c1" style="top:2284px">
  <span class="mini-brand">MORVANT</span>
  <div class="s-title center" style="top:16px;font-size:11px">Process</div>
  <svg class="ph" style="left:128px;top:40px" width="84" height="84" viewBox="0 0 84 84">
    <circle cx="42" cy="42" r="30" fill="none" stroke="var(--purple)" stroke-width="16" stroke-dasharray="44 144"/>
    <circle cx="42" cy="42" r="30" fill="none" stroke="var(--gold)" stroke-width="16" stroke-dasharray="44 144" stroke-dashoffset="-47"/>
    <circle cx="42" cy="42" r="30" fill="none" stroke="var(--purple)" stroke-width="16" stroke-dasharray="44 144" stroke-dashoffset="-94"/>
    <circle cx="42" cy="42" r="30" fill="none" stroke="var(--gold)" stroke-width="16" stroke-dasharray="44 144" stroke-dashoffset="-141"/>
  </svg>
  <div class="t" style="left:24px;top:50px"><b>Step one</b>Short line</div><div class="t" style="left:24px;top:100px"><b>Step two</b>Short line</div>
  <div class="t" style="left:240px;top:50px"><b>Step three</b>Short line</div><div class="t" style="left:240px;top:100px"><b>Step four</b>Short line</div>
  <div class="foot"><span class="flag"></span><span>Funded under grant agreement 000000</span></div>
</div>
<div class="slide c2" style="top:2284px;background:linear-gradient(135deg,#fff 50%,var(--lilac-soft))">
  <span class="mini-brand">MORVANT</span>
  <div class="s-title" style="left:30px;top:60px;font-size:20px">THANK YOU</div>
  <div class="chip" style="left:190px;top:50px;width:9px;height:9px;background:var(--purple)"></div><div class="t" style="left:205px;top:50px">info@morvant.example</div>
  <div class="chip" style="left:190px;top:72px;width:9px;height:9px;background:var(--purple)"></div><div class="t" style="left:205px;top:72px">+00 000 000 000</div>
  <div class="chip" style="left:190px;top:94px;width:9px;height:9px;background:var(--purple)"></div><div class="t" style="left:205px;top:94px">www.morvant.example</div>
  <div class="foot"><span class="flag"></span><span>Funded under grant agreement 000000</span></div>
</div>
<div class="slide c3" style="top:2284px">
  <span class="mini-brand">MORVANT</span>
  <div class="s-title center" style="top:18px;font-size:11px">Bullet Point</div>
  <ul class="list" style="left:30px;top:44px"><li>Add a key point</li><li>Add a key point</li><li>Add a key point</li><li>Add a key point</li></ul>
  <ul class="list purple" style="left:180px;top:44px"><li>Add a key point</li><li>Add a key point</li><li>Add a key point</li><li>Add a key point</li></ul>
  <div class="foot"><span class="flag"></span><span>Funded under grant agreement 000000</span></div>
</div>

<!-- ===== row 10 ===== -->
<div class="slide c1" style="top:2482px">
  <span class="mini-brand">MORVANT</span>
  <div class="s-title center" style="top:16px;font-size:11px">Process</div>
  <svg class="ph" style="left:128px;top:40px" width="84" height="84" viewBox="0 0 84 84">
    <rect x="6" y="6" width="34" height="34" rx="6" fill="var(--purple)"/><rect x="44" y="6" width="34" height="34" rx="6" fill="var(--gold)"/>
    <rect x="6" y="44" width="34" height="34" rx="6" fill="var(--gold)"/><rect x="44" y="44" width="34" height="34" rx="6" fill="var(--purple)"/>
  </svg>
  <div class="t" style="left:24px;top:50px"><b>Step one</b>Short line</div><div class="t" style="left:24px;top:100px"><b>Step two</b>Short line</div>
  <div class="t" style="left:240px;top:50px"><b>Step three</b>Short line</div><div class="t" style="left:240px;top:100px"><b>Step four</b>Short line</div>
  <div class="foot"><span class="flag"></span><span>Funded under grant agreement 000000</span></div>
</div>
<div class="slide c2" style="top:2482px">
  <div class="logo-lock" style="left:82px;top:64px"><span class="dot" style="width:26px;height:26px"></span><span class="nm" style="font-size:22px">MORVANT</span></div>
  <div class="t center" style="top:98px">Gender Equality in STEM Research</div>
  <div class="foot"><span class="flag"></span><span>Funded under grant agreement 000000</span></div>
</div>

</body>
</html>
```